Safety Brochure for Industry Assocations

This is an 8.5 x 11 single sided brochure for our Occupational Health and Safety Data Analytics software. If you need to use stock images we will pay for them.

Please incorporate our logo and some of the images. No need to incorporate them all. We like the idea of the boots being at the bottom of the page but we're open to other ideas.

Please note that we intend to mail this brochure to different industries so it should be generic (i.e. not construction specific).

Target Market(s)

Safety and Industry Organisations for construction, mining, forestry and oil and gas industries.

Industry/Entity Type

Industry

Font styles to use
Sans Serif

Colors

Designer to choose colors to be used in the design.

Requirements
Must have
• We are a software company that produces safety software. Our customers are companies that engage in dangerous work and use our software to improve their worker's safety. The look and feel should convey the fact that:
• -We are Big Data
• -We are Software
• -We service industry
Nice to have
• Please see the Pixfold photo of the boots. We were hoping that the desiger would be able ti modify the image with an overlay of 0's and 1's in a kind of "matrix" fashion to indicate that we are merging traditional labour work with software.
Should not have
• No medical symbols. Note that WE ARE NOT HEALTH CARE.

```html
<!DOCTYPE html>
<html lang="en">
<head>
<meta charset="utf-8">
<title>Fieldsafe Analytics – Safety Data Brochure</title>
<link href="https://fonts.googleapis.com/css2?family=Montserrat:wght@400;600;700&family=Oswald:wght@500;600&display=swap" rel="stylesheet">
<style>
  :root {
    --green: #20a346;
    --green-bright: #4cb848;
    --lime: #8dc63f;
    --charcoal: #3d3d3d;
    --dark-panel: #2f3132;
    --ink: #333333;
    --paper: #ffffff;
    --mist: #f1f2f1;
    --backdrop: #e4e4e4;
    --bullet: #c8e03a;
    --screen-light: #e9ebea;
    --screen-mid: #b9bcbb;
    --leather-light: #7a5a3e;
    --leather-dark: #4a3322;
  }
  * { box-sizing: border-box; margin: 0; padding: 0; }
  html, body { width: 1200px; height: 1200px; overflow: hidden; }
  body { background: var(--backdrop); font-family: "Montserrat", sans-serif; color: var(--ink); position: relative; }

  .brochure { position: absolute; left: 175px; top: 50px; width: 850px; height: 1100px; background: var(--paper); overflow: hidden; box-shadow: 0 4px 18px rgba(0,0,0,.18); }

  /* header */
  .brand { position: absolute; left: 38px; top: 36px; display: flex; align-items: center; gap: 14px; }
  .brand-dot { width: 70px; height: 70px; border-radius: 50%; background: var(--green); }
  .brand-name { font-weight: 600; font-size: 25px; line-height: 1.05; color: var(--charcoal); letter-spacing: 3px; }
  .contact { position: absolute; left: 508px; top: 30px; }
  .contact-title { font-weight: 700; font-size: 36px; color: var(--green); }
  .contact-phone { display: flex; align-items: center; gap: 10px; margin-top: 8px; font-size: 28px; color: var(--ink); }

  /* green band */
  .hero-band { position: absolute; left: 0; top: 162px; width: 850px; height: 292px; background: var(--green); }
  .hero-panel { position: absolute; left: 0; top: 162px; width: 850px; height: 292px; }
  .hero-copy { position: absolute; left: 46px; top: 182px; width: 400px; color: #fff; }
  .hero-kicker { font-size: 22px; letter-spacing: 1px; }
  .hero-title { font-family: "Oswald", sans-serif; font-weight: 500; font-size: 40px; line-height: 1.2; margin-top: 2px; }
  .hero-list { list-style: none; margin-top: 18px; font-size: 12.5px; line-height: 1.35; }
  .hero-list li { position: relative; padding-left: 22px; margin-bottom: 9px; }
  .hero-list li::before { content: ""; position: absolute; left: 2px; top: 5px; width: 7px; height: 7px; border-radius: 50%; background: var(--bullet); }
  .hero-list b { font-weight: 700; }
  .devices-photo { position: absolute; left: 440px; top: 212px; width: 380px; height: 290px; border-radius: 6px; background: linear-gradient(160deg, var(--screen-light), var(--screen-mid)); }

  /* diagram */
  .diagram-area { position: absolute; left: 0; top: 454px; width: 850px; height: 460px; background: linear-gradient(180deg, var(--paper), var(--mist) 55%, var(--paper)); }
  .diagram { position: absolute; left: 0; top: 454px; }
  .node { position: absolute; text-align: center; color: var(--ink); }
  .node-core { left: 372px; top: 520px; width: 100px; font-weight: 600; font-size: 20px; letter-spacing: 4px; line-height: 1.1; }
  .node-core span { display: block; font-size: 16px; letter-spacing: 1px; }
  .node-title { font-weight: 700; font-size: 15px; line-height: 1.2; margin-bottom: 6px; }
  .node-list { list-style: none; text-align: left; font-size: 10.5px; line-height: 1.3; }
  .node-list li { position: relative; padding-left: 11px; margin-bottom: 4px; }
  .node-list li::before { content: ""; position: absolute; left: 0; top: 5px; width: 4px; height: 4px; border-radius: 50%; background: var(--ink); }
  .node-training { left: 98px; top: 700px; width: 130px; }
  .node-bench { left: 356px; top: 704px; width: 134px; }
  .node-trend { left: 604px; top: 694px; width: 132px; }

  /* footer */
  .footer-shape { position: absolute; left: 0; top: 912px; }
  .footer-copy { position: absolute; left: 46px; top: 935px; color: #fff; }
  .footer-step { font-family: "Oswald", sans-serif; font-weight: 500; font-size: 30px; color: var(--charcoal); line-height: 1.1; }
  .footer-sub { font-size: 15px; margin-top: 2px; }
  .footer-industry { font-family: "Oswald", sans-serif; font-weight: 500; font-size: 40px; line-height: 1.15; }
  .footer-contacts { position: absolute; left: 46px; top: 1060px; display: flex; gap: 22px; color: #fff; font-size: 11px; }
  .footer-contacts span { display: flex; align-items: center; gap: 6px; }
  .boots-photo { position: absolute; left: 560px; top: 912px; width: 268px; height: 140px; border-radius: 6px 6px 0 0; background: linear-gradient(180deg, var(--leather-light), var(--leather-dark)); }
</style>
</head>
<body>
<main class="brochure">

  <header>
    <div class="brand">
      <div class="brand-dot"></div>
      <div class="brand-name">Fieldsafe<br>Analytics</div>
    </div>
    <div class="contact">
      <div class="contact-title">Call Us At</div>
      <div class="contact-phone">
        <svg width="22" height="22" viewBox="0 0 24 24"><path d="M6.6 10.8a15 15 0 0 0 6.6 6.6l2.2-2.2a1 1 0 0 1 1-.25 11.4 11.4 0 0 0 3.6.57 1 1 0 0 1 1 1V20a1 1 0 0 1-1 1A17 17 0 0 1 3 4a1 1 0 0 1 1-1h3.5a1 1 0 0 1 1 1c0 1.25.2 2.45.57 3.57a1 1 0 0 1-.25 1z" fill="#20a346"/></svg>
        1-888-555-0142
      </div>
    </div>
  </header>

  <section class="hero">
    <div class="hero-band"></div>
    <svg class="hero-panel" width="850" height="292" viewBox="0 0 850 292">
      <polygon points="405,0 850,0 850,292 480,292 448,238 448,150" fill="var(--dark-panel)"/>
    </svg>
    <div class="hero-copy">
      <div class="hero-kicker">Leverage the power of</div>
      <div class="hero-title">BIG DATA</div>
      <ul class="hero-list">
        <li><b>LEAD</b> the next wave of injury reduction</li>
        <li><b>ENGAGE</b> with members through collaboration<br>and benchmarking</li>
        <li><b>PROMOTE</b> standardization</li>
        <li><b>ANALYZE</b> Accurate, Timely and Complete Leading<br>Indicators</li>
        <li><b>TRAIN</b> industry more proactively</li>
      </ul>
    </div>
    <div class="devices-photo" role="img" aria-label="Photo of a desktop monitor and laptop showing safety data bar and pie charts"></div>
  </section>

  <section>
    <div class="diagram-area"></div>
    <svg class="diagram" width="850" height="460" viewBox="0 0 850 460">
      <g stroke="#333" stroke-width="2">
        <line x1="365" y1="120" x2="255" y2="210"/>
        <line x1="422" y1="132" x2="422" y2="175"/>
        <line x1="480" y1="120" x2="585" y2="210"/>
      </g>
      <g fill="#fff" stroke-width="11">
        <circle cx="422" cy="82" r="52" stroke="#dcdcdc"/>
        <circle cx="422" cy="82" r="52" stroke="var(--green)" stroke-dasharray="245 82" transform="rotate(-60 422 82)"/>
      </g>
      <g fill="#fff" stroke-width="16">
        <circle cx="163" cy="308" r="90" stroke="var(--charcoal)"/>
        <circle cx="163" cy="308" r="90" stroke="var(--green-bright)" fill="none" stroke-dasharray="283 283" transform="rotate(175 163 308)"/>
        <circle cx="422" cy="308" r="90" stroke="var(--green-bright)"/>
        <circle cx="422" cy="308" r="90" stroke="var(--lime)" fill="none" stroke-dasharray="283 283" transform="rotate(175 422 308)"/>
        <circle cx="668" cy="308" r="90" stroke="var(--charcoal)"/>
        <circle cx="668" cy="308" r="90" stroke="var(--green-bright)" fill="none" stroke-dasharray="283 283" transform="rotate(175 668 308)"/>
      </g>
    </svg>
    <div class="node node-core">EHS<span>DATA</span></div>
    <div class="node node-training">
      <div class="node-title">Training</div>
      <ul class="node-list"><li>Analyze needs of Industry</li><li>Deliver Proactive Training</li><li>Improve Safety</li></ul>
    </div>
    <div class="node node-bench">
      <div class="node-title">Benchmarking</div>
      <ul class="node-list"><li>Engage with Members</li><li>Promote Collaborative Advancement of Safety</li><li>Improve Safety</li></ul>
    </div>
    <div class="node node-trend">
      <div class="node-title">Trend<br>Analysis</div>
      <ul class="node-list"><li>Monitor Industry Trends</li><li>Implement Corrective Initiatives</li><li>Improve Safety</li></ul>
    </div>
  </section>

  <footer>
    <div class="boots-photo" role="img" aria-label="Photo of a pair of worn brown leather work boots"></div>
    <svg class="footer-shape" width="850" height="188" viewBox="0 0 850 188">
      <polygon points="0,0 368,0 470,140 850,140 850,188 0,188" fill="var(--green)"/>
    </svg>
    <div class="footer-copy">
      <div class="footer-step">THE NEXT BIG STEP</div>
      <div class="footer-sub">in injury reduction for your</div>
      <div class="footer-industry">ENTIRE INDUSTRY</div>
    </div>
    <div class="footer-contacts">
      <span><svg width="12" height="12" viewBox="0 0 12 12"><circle cx="6" cy="6" r="5" fill="none" stroke="#fff" stroke-width="1.4"/><path d="M1 6h10M6 1c2 2 2 8 0 10M6 1c-2 2-2 8 0 10" stroke="#fff" fill="none"/></svg>www.fieldsafedata.com</span>
      <span><svg width="10" height="13" viewBox="0 0 10 13"><path d="M5 0a5 5 0 0 1 5 5c0 3.5-5 8-5 8S0 8.5 0 5a5 5 0 0 1 5-5z" fill="#fff"/><circle cx="5" cy="5" r="1.8" fill="#20a346"/></svg>Suite # 210 - 518 Ridge Ave SW Northvale AB T0X 1A0</span>
    </div>
  </footer>

</main>
</body>
</html>
```